Wedding design templates - fresh

We require 3 different wedding designs. I have attached the watercolour images for the graphic designer to use on each template. I want to be able to easily change the name and location of the invitation when needed and be able to freely use whatever font is used, so that the invite becomes our template. I want something fresh with a modern layout but on a white background. The use of coloured fonts are okay to suit the images provided. The size of the card stock is A5 (half of an A4) please consider bleeds etc for printing.

Target Market(s)

Bridal market - young couples

Industry/Entity Type

Wedding

Font styles to use
Serif
Sans Serif
Script

Requirements
Must have
• Be able to use fonts and change details easily. common colours that can easily fit in with a brides colour scheme. must have all details for wedding invites ie church name address etc can be any church or reception place in sydney
Nice to have
• i have uploaded some example images as to style i am looking for.
• I want to be able to run a theme with these images eg. rsvp cards, place cards etc

```html
<!DOCTYPE html>
<html lang="en">
<head>
<meta charset="utf-8">
<title>Wedding Invitation – Watercolour Floral</title>
<link rel="stylesheet" href="https://fonts.googleapis.com/css2?family=Kaushan+Script&family=Source+Sans+3:ital,wght@0,400;1,400&display=swap">
<style>
  :root {
    --backdrop: #e9e7e4;
    --card: #ffffff;
    --names-green: #8a9b3c;
    --text-mauve: #7b4b61;
    --petal-pink: #f3cdd7;
    --petal-blue: #c3dbe1;
    --leaf-green: #cfe0cb;
    --bloom-cream: #f4f0df;
  }
  * { box-sizing: border-box; margin: 0; padding: 0; }
  html, body {
    width: 1200px;
    height: 1000px;
    overflow: hidden;
    background: var(--backdrop);
  }
  .invitation {
    position: absolute;
    left: 284px;
    top: 42px;
    width: 624px;
    height: 888px;
    background: var(--card);
    box-shadow: 0 1px 4px rgba(0,0,0,0.08);
  }
  .floral {
    position: absolute;
    border-radius: 50%;
    background: linear-gradient(90deg,
      var(--leaf-green) 0%,
      var(--petal-blue) 28%,
      var(--petal-pink) 50%,
      var(--petal-blue) 72%,
      var(--leaf-green) 100%);
  }
  .floral--top {
    left: 91px;
    top: 43px;
    width: 425px;
    height: 170px;
  }
  .floral--bottom {
    left: 66px;
    top: 643px;
    width: 485px;
    height: 205px;
  }
  .couple-names {
    position: absolute;
    left: 0;
    top: 240px;
    width: 100%;
    padding-left: 24px;
    text-align: center;
    font-family: "Kaushan Script", cursive;
    font-size: 78px;
    font-weight: 400;
    line-height: 1;
    color: var(--names-green);
    white-space: nowrap;
  }
  .invite-lead {
    position: absolute;
    left: 0;
    top: 369px;
    width: 100%;
    padding-left: 24px;
    text-align: center;
    font-family: "Source Sans 3", sans-serif;
    font-size: 19.5px;
    color: var(--text-mauve);
  }
  .guest-line {
    position: absolute;
    left: 126px;
    top: 432px;
    width: 398px;
    border-top: 2px dotted var(--text-mauve);
  }
  .event-details {
    position: absolute;
    left: 0;
    top: 440px;
    width: 100%;
    padding-left: 24px;
    text-align: center;
    font-family: "Source Sans 3", sans-serif;
    font-size: 19.5px;
    line-height: 23.5px;
    color: var(--text-mauve);
  }
  .event-details .reception {
    font-style: italic;
  }
</style>
</head>
<body>
  <main class="invitation">
    <div class="floral floral--top" role="img" aria-label="Watercolour spray of a pink anemone, blue blossoms, green sprigs and cream star flowers"></div>

    <h1 class="couple-names">Clara &amp; Matteo</h1>

    <p class="invite-lead">wish to invite</p>
    <div class="guest-line" aria-hidden="true"></div>

    <div class="event-details">
      <p>to join them as they celebrate their marriage</p>
      <p>on Saturday 18th July 2015</p>
      <p>at three in the afternoon</p>
      <p>in ST. ELIZABETH'S CHAPEL,</p>
      <p>Sydney.</p>
      <p class="reception">Reception to follow.</p>
    </div>

    <div class="floral floral--bottom" role="img" aria-label="Watercolour spray of a pink anemone, blue blossoms, green sprigs and cream star flowers"></div>
  </main>
</body>
</html>
```